Professional window cleaning services business needs a flyer design

We are looking to attract large businesses such as gyms, car dealerships and fast food restaurants.
-Have over 15 years of experience in this business
-We serve customers in Melbourne and all surrounding suburbs
-Specialising in automated periodical services(daily,weekly,monthly, yearly)
-Our current client base consists of major fast food restaurants, car dealerships and residential properties.

Industry/Entity Type

Window Cleaning

Colors
3176b5
fbed22

Requirements
Must have
• Business Details:
• Name: Brightpane Window Cleaning
• Phone no:95402367
• website:www.quorlinpro.com.au
• email: admin@quorlinpro.com.au
• mail: PO BOX 4826, Marrowdale Heights, 3478

```html
<!DOCTYPE html>
<html lang="en">
<head>
<meta charset="utf-8">
<title>Brightpane Window Cleaning</title>
<link rel="stylesheet" href="https://fonts.googleapis.com/css2?family=Dancing+Script:wght@500&family=Varela+Round&display=swap">
<style>
  :root {
    --navy: #2b2e6e;
    --sky-pale: #e3f2fb;
    --sky-light: #a9d8f2;
    --sky-mid: #5fb9e8;
    --sky-deep: #3176b5;
    --white: #ffffff;
  }
  * { margin: 0; padding: 0; box-sizing: border-box; }
  html, body { width: 848px; height: 1200px; overflow: hidden; background: var(--white); }
  .flyer {
    position: relative;
    width: 848px;
    height: 1200px;
    overflow: hidden;
    background: var(--white);
    font-family: "Varela Round", sans-serif;
    color: var(--navy);
  }
  .backdrop { position: absolute; inset: 0; }
  .tagline-experience {
    position: absolute;
    left: 440px;
    top: 92px;
    font-family: "Dancing Script", cursive;
    font-size: 30px;
    color: var(--navy);
    transform: rotate(20deg);
    transform-origin: left top;
    white-space: nowrap;
    letter-spacing: 1px;
  }
  .tagline-experience .big { font-size: 40px; }
  .staff-note {
    position: absolute;
    left: 370px;
    top: 283px;
    width: 340px;
    text-align: center;
    color: var(--white);
    font-size: 13.5px;
    line-height: 16.5px;
  }
  .brand { position: absolute; left: 84px; top: 470px; }
  .brand-name { font-size: 80px; line-height: 1; letter-spacing: -1px; }
  .brand-sub { font-size: 38px; line-height: 1; margin-top: 6px; letter-spacing: -0.5px; }
  .area {
    position: absolute;
    left: 80px;
    top: 622px;
    font-family: "Dancing Script", cursive;
    font-size: 24px;
    line-height: 36px;
    transform: skewX(-8deg);
  }
  .call { position: absolute; left: 86px; top: 718px; }
  .call-label { font-size: 27px; line-height: 1; }
  .call-number { font-size: 40px; line-height: 1.05; }
  .info { position: absolute; left: 81px; font-size: 14.5px; line-height: 17.5px; }
  .info-services { top: 817px; }
  .info-clients { top: 875px; }
  .info-email { top: 998px; }
  .info-mail { top: 1057px; }
  .website { position: absolute; left: 81px; top: 1112px; font-size: 23px; }
</style>
</head>
<body>
<main class="flyer">
  <svg class="backdrop" width="848" height="1200" viewBox="0 0 848 1200" xmlns="http://www.w3.org/2000/svg">
    <defs>
      <linearGradient id="vanPhoto" x1="0" y1="0" x2="1" y2="1">
        <stop offset="0" stop-color="#c9c6b4"/>
        <stop offset="0.5" stop-color="#d8c23a"/>
        <stop offset="1" stop-color="#5e5a4c"/>
      </linearGradient>
      <linearGradient id="glassPhoto" x1="0" y1="0" x2="1" y2="1">
        <stop offset="0" stop-color="#6f9fd0"/>
        <stop offset="0.5" stop-color="#2f5f9c"/>
        <stop offset="1" stop-color="#1f3c66"/>
      </linearGradient>
      <linearGradient id="fleetPhoto" x1="0" y1="0" x2="1" y2="1">
        <stop offset="0" stop-color="#5b6a52"/>
        <stop offset="0.5" stop-color="#dfe3ea"/>
        <stop offset="1" stop-color="#3d4148"/>
      </linearGradient>
    </defs>

    <path d="M0 0 H120 C150 300 300 700 848 980 V1200 H0 Z" fill="var(--sky-pale)"/>
    <path d="M0 0 H60 C80 260 120 420 60 600 C30 700 10 760 0 800 Z" fill="var(--sky-light)" opacity="0.7"/>

    <path role="img" aria-label="Photo: team member standing beside a yellow branded service van"
          d="M106 0 H470 L560 150 L165 268 Z" fill="url(#vanPhoto)"/>
    <path role="img" aria-label="Photo: rope-access crew abseiling down a glass office facade"
          d="M165 268 L560 150 L848 150 V372 L350 490 Z" fill="url(#glassPhoto)"/>
    <path role="img" aria-label="Photo: two uniformed staff beside branded utility vehicles with ladders"
          d="M350 490 L848 372 V830 C700 760 560 650 440 560 Z" fill="url(#fleetPhoto)"/>

    <path d="M420 40 C560 120 700 170 848 200 V0 H400 Z" fill="var(--sky-light)" opacity="0.9"/>
    <path d="M440 60 C580 150 720 190 848 210 V190 C720 170 580 130 460 50 Z" fill="var(--white)" opacity="0.8"/>
    <path d="M120 0 C150 180 220 360 340 520 C300 380 220 200 175 0 Z" fill="var(--sky-mid)" opacity="0.55"/>
    <path d="M60 600 C200 650 380 720 520 760 C680 800 780 810 848 800 V860 C700 860 520 820 340 740 C220 690 120 640 60 600 Z" fill="var(--sky-mid)" opacity="0.45"/>
    <path d="M380 820 C560 900 720 930 848 920 V1200 H600 C700 1100 560 950 380 820 Z" fill="var(--sky-light)" opacity="0.85"/>
    <path d="M500 900 C650 980 760 1000 848 990 V1200 H760 C780 1100 680 980 500 900 Z" fill="var(--sky-mid)" opacity="0.6"/>
    <path d="M300 860 C450 960 560 1080 600 1200 H650 C610 1070 480 950 300 860 Z" fill="var(--sky-light)" opacity="0.6"/>
  </svg>

  <p class="tagline-experience">Over <span class="big">15</span> years of experience</p>

  <p class="staff-note">Our staff are fully trained<br>and uniformed<br>and are capable of working<br>on all types of sites –<br>from ground to multi level structures.<br>We hold all appropriate tickets for abseiling<br>and operating booms etc. and have full<br>insurances for public liability and Workcover.</p>

  <header class="brand">
    <h1 class="brand-name">Brightpane</h1>
    <p class="brand-sub">Window Cleaning</p>
  </header>

  <p class="area">We serve customers in Melbourne<br>and all surrounding suburbs</p>

  <div class="call">
    <p class="call-label">Call us now:</p>
    <p class="call-number">95402367</p>
  </div>

  <p class="info info-services">Specialising in automated periodical services<br>(daily,weekly,monthly, yearly)</p>
  <p class="info info-clients">Our current client base consists of<br>major fast food restaurants,<br>car dealerships and<br>residential properties.</p>
  <p class="info info-email">Email:<br>admin@quorlinpro.com.au</p>
  <p class="info info-mail">Mail:<br>PO BOX 4826, Marrowdale Heights, 3478</p>
  <p class="website">www.quorlinpro.com.au</p>
</main>
</body>
</html>
```